New online business - used mobile phones - needs unique eye catching web design that sets it apart

The Handset Bazaar
We are a new business looking for a rapid response for our web site design. We don't want a normal website....... we need to be creative - most important PLEASE view the attached files uploaded 3 March to ensure you get us :)
.
The Handset Bazaar buys new and damaged mobile phones from the public. A simple process they complete to sell their mobile to us; we want our website to reflect this.
Our website needs to be modern, edgy and fun, not corporate and definitely not like any other mobile phone buying site in the world today!!
Our name was taken from a play on the share/stock market which we have tried to bring into the design ....... it hasn't worked with early designs submitted. Now taking a different approach. Refer to new attached files which should help you visualise our concept.

We like layout from Sketch Flock – rtlbenoviqs #7132809 design as this is very close to our layout vision.
The first page to tell the public what we do, how we do it, and then they click to accept the instant online quote. (page two they complete details about the mobiles model & condition they are selling, then page three complete their personal details).
Our background preference is dark, blackboard or dark with slight texture
a) We love white on black/dark background either typewriter font or look like hand drawn refer to attached files & heronandfig.com.au site to see. Would Label font work???

b) Where the light blue colour is on #7132809 this needs to be like chromavell colour classic green, fern green or bright green, not fluorescent lime green or an insipid green.

c) The banner says The Handset Bazaar is open........... for buying mobiles for cash $$$ (we need people to know we BUY used/damaged phones)

d) We love colour either solid colour or looks like it has been coloured in on our dark background. Open to white or pastel background versions refer to attached coffee file.
We like Chromavell Orange 021,Haute Red,Dazzling Blue, Cyan Blue, Beetroot Purple, Island Green.
e) How it works – underneath this title put Our deal …………. It’s easy as…………..quote, post, get paid!!!
Quote – first circle hand drawn icon showing mobile phone & $ sign. Underneath it says .....Obtain Quote for Model & Condition
Post – second circle hand drawn icon show parcel. Underneath it says Free Post
Paid – third circle hand drawn icon showing large $ sign. Underneath it says Payment in Two Days
Plans - is swapped for wording- Get Market Quote with a large button which says GO or CLICK HERE (they click on the button & it takes them to the next page)
f) FAQ
Allow for six FAQ’s we will forward correct content to you for final design layout.

g) About Us
Please allow about a paragraph of text here, we will forward correct content to you for final design layout.
h) Contact Us
At the bottom where normal website have ………. home, contact details, blog, etc, please only put Email us & Call us, then social media icons for QV, Work Nest and Chirpel

I) LOGO We don’t have one yet, just put The Handset Bazaar at the top & it needs to be large sized font ................we are new and we need to push our name
If you are not clear on our vision ..........please email me and I will reply very quickly.
Thank you for taking the time to read & understand & get us:)

Target Market(s)

20-45 years any body with a spare smart phone that is lying around and they can get cash for. Target market could be slightly older to 50 but focus of 20-40's

Industry/Entity Type

Business

Number of Pages Required

3 page

Font styles to use
Other font styles liked:
• handwritten font or typewriter font

Requirements
Must have
• Read only attached files dated 4 March, tech error with other files, being removed.
• 1 Layout design of Sketch Flock – rtlbenoviqs #7132809
• 2 Hand drawn icons - refer to files
• 3 White font needs to look like hand written refer to heronandfig.com.au or typewriter font - large size font
• 4 Main colours are Black or dark background, green with white text, preference is hand drawn font. The three circles for quote, post & pay with hand drawn icons can be any colour ...... Purple for quote, orange for post & green for paid
• 5 Big green button underneath 3 circles quote/post/pay - customers click on big button to get instant quote
Nice to have
• Coloured in hand drawings as per file
• Great Hand drawings coloured in
Should not have
• NO template designs so it look like you just put some text & a photo. Don't fill the page with mobile phones, one or two is ok, mobile phone pictures date so fast.
• Cartoons

```html
<!DOCTYPE html>
<html lang="en">
<head>
<meta charset="utf-8">
<title>The Handset Bazaar</title>
<link rel="stylesheet" href="https://fonts.googleapis.com/css2?family=Delius&family=Signika:wght@600&family=Open+Sans:wght@400;600&display=swap">
<style>
:root{
  --green:#17a86a;
  --green-dark:#128a57;
  --ink:#333;
  --muted:#777;
  --line:#ddd;
  --soft:#f5f5f5;
  --footer:#1b1b1b;
  --white:#fff;
}
*{box-sizing:border-box;margin:0;padding:0}
html,body{width:682px;height:1200px;overflow:hidden;background:var(--white)}
body{position:relative;font-family:"Open Sans",sans-serif;color:var(--ink)}
.site-header{position:absolute;top:0;left:0;width:682px;height:49px;background:var(--green);display:flex;align-items:center;justify-content:center}
.brand{font-family:"Signika",sans-serif;font-weight:600;font-size:24px;color:var(--white)}
.main-nav{position:absolute;top:49px;left:0;width:682px;height:27px;display:flex;justify-content:center;align-items:center;gap:23px;border-bottom:1px solid #e6e6e6}
.main-nav a{font-size:7.5px;text-transform:uppercase;color:#888;text-decoration:none;letter-spacing:.2px}
.main-nav a.active{color:var(--green);font-weight:600}
.hero{position:absolute;top:76px;left:0;width:682px;height:297px;background:radial-gradient(ellipse at 30% 40%,#3a1e1a 0%,#1c1410 45%,#0d0b0a 100%),#111;overflow:hidden}
.hero-photo{position:absolute;inset:0;background:linear-gradient(100deg,rgba(120,20,20,.35) 0%,rgba(40,40,90,.3) 35%,rgba(150,100,20,.35) 65%,rgba(90,60,10,.3) 100%)}
.hero-copy{position:absolute;top:98px;left:0;width:682px;text-align:center;font-family:"Delius",cursive;color:var(--white)}
.hero-copy h1{font-weight:400;font-size:23px;line-height:29px}
.hero-btn{display:inline-block;margin-top:14px;border:1.5px solid var(--white);padding:6px 9px;font-size:10px;color:var(--white)}
.slide-arrow{position:absolute;top:141px;width:17px;height:17px;background:rgba(40,40,40,.85)}
.slide-arrow.prev{left:0}.slide-arrow.next{right:0}
.slide-arrow svg{width:17px;height:17px}
.steps-title{position:absolute;top:402px;left:0;width:682px;text-align:center;font-family:"Delius",cursive;font-size:13px;color:var(--ink)}
.step{position:absolute;top:434px;width:150px;text-align:center;font-family:"Delius",cursive}
.step svg{display:block;margin:0 auto}
.step h3{font-weight:400;font-size:17px;color:var(--green);margin-top:4px;line-height:20px}
.step p{font-size:7.5px;color:#555;line-height:12px}
.step-arrow{position:absolute;top:469px}
.divider{position:absolute;top:597px;left:56px;width:569px;border-top:1px solid var(--line)}
.get-market{position:absolute;top:622px;left:143px;width:310px}
.get-market h2{font-family:"Delius",cursive;font-weight:400;font-size:16px;color:var(--green)}
.get-market p{font-size:6.3px;line-height:11px;color:var(--muted);margin-top:3px}
.go-btn{display:inline-block;margin-top:7px;background:var(--green);color:var(--white);font-family:"Delius",cursive;font-size:12px;padding:3px 7px;border-radius:2px}
.market-mark{position:absolute;top:642px;left:474px;width:64px;height:64px;border-radius:50%;background:radial-gradient(circle,#444 0 8%,#fff 9% 22%,#444 23% 33%,#fff 34% 48%,#444 49% 60%,#fff 61% 75%,#444 76% 100%)}
.faq{position:absolute;top:748px;left:0;width:682px;height:243px;background:var(--soft);border-top:1px solid #e6e6e6;border-bottom:1px solid #e6e6e6}
.section-title{font-family:"Delius",cursive;font-weight:400;font-size:16px;color:var(--green);text-align:center}
.faq .section-title{margin-top:22px}
.faq-grid{position:absolute;top:56px;left:62px;width:560px;display:grid;grid-template-columns:repeat(3,1fr);column-gap:50px;row-gap:18px}
.faq-item{text-align:center}
.faq-item h4{font-family:"Delius",cursive;font-weight:400;font-size:8.8px;line-height:12.5px;color:#333}
.faq-item p{font-size:6px;line-height:9px;color:var(--muted);margin-top:3px}
.about{position:absolute;top:1015px;left:90px;width:502px;text-align:center}
.about p{font-size:6.6px;line-height:11.7px;color:var(--muted);margin-top:6px}
.site-footer{position:absolute;top:1122px;left:0;width:682px;height:78px;background:var(--footer);color:#bbb;font-size:6.4px}
.footer-links{position:absolute;top:16px;left:56px}
.footer-links a{color:#ccc;text-decoration:none}
.footer-links span{color:#666;margin:0 4px}
.copyright{position:absolute;top:34px;left:56px}
.contact{position:absolute;top:51px;left:56px}
.socials{position:absolute;top:30px;right:56px;display:flex;gap:9px}
.social{display:flex;align-items:center;gap:3px;color:#ccc;font-size:6.4px}
.social i{display:block;width:7px;height:7px;border-radius:50%;background:#555}
</style>
</head>
<body>
<header class="site-header"><div class="brand">The Handset Bazaar</div></header>
<nav class="main-nav">
  <a class="active" href="#">Home</a><a href="#">Quote</a><a href="#">Order</a><a href="#">Testimonials</a><a href="#">Contact</a><a href="#">Login</a>
</nav>

<section class="hero">
  <div class="hero-photo" role="img" aria-label="Dark photo of a glowing stock market price board with red, orange and blue digits"></div>
  <div class="hero-copy">
    <h1>The Handset Bazaar is open for<br>buying mobiles for cash</h1>
    <span class="hero-btn">Know more</span>
  </div>
  <div class="slide-arrow prev"><svg viewBox="0 0 17 17"><path d="M12 8.5H5M8 5.5 5 8.5l3 3" stroke="#ccc" stroke-width="1.6" fill="none"/></svg></div>
  <div class="slide-arrow next"><svg viewBox="0 0 17 17"><path d="M5 8.5h7M9 5.5l3 3-3 3" stroke="#ccc" stroke-width="1.6" fill="none"/></svg></div>
</section>

<h2 class="steps-title">Our deal …&nbsp; It’s easy as …&nbsp;&nbsp; Quote, Post, Get paid!!!</h2>

<div class="step" style="left:113px">
  <svg width="90" height="90" viewBox="0 0 90 90"><circle cx="45" cy="45" r="43" fill="none" stroke="#ccc"/>
    <rect x="24" y="25" width="17" height="30" rx="2" fill="none" stroke="#17a86a" stroke-width="2"/>
    <circle cx="51" cy="48" r="10" fill="none" stroke="#17a86a" stroke-width="2"/>
    <text x="51" y="52" text-anchor="middle" font-family="Open Sans,sans-serif" font-size="11" font-weight="600" fill="#17a86a">$</text></svg>
  <h3>Quote</h3><p>Obtain quote for model &amp; condition.</p>
</div>
<svg class="step-arrow" style="left:249px" width="30" height="18" viewBox="0 0 30 18"><path d="M1 6h18V2l9 7-9 7v-4H1z" fill="#f2f2f2" stroke="#999"/></svg>
<div class="step" style="left:264px">
  <svg width="90" height="90" viewBox="0 0 90 90"><circle cx="45" cy="45" r="43" fill="none" stroke="#ccc"/>
    <rect x="30" y="36" width="30" height="18" fill="none" stroke="#17a86a" stroke-width="2"/>
    <path d="M35 45h20" stroke="#17a86a" stroke-width="1.5"/></svg>
  <h3>Post</h3><p>Free post</p>
</div>
<svg class="step-arrow" style="left:400px" width="30" height="18" viewBox="0 0 30 18"><path d="M1 6h18V2l9 7-9 7v-4H1z" fill="#f2f2f2" stroke="#999"/></svg>
<div class="step" style="left:416px">
  <svg width="90" height="90" viewBox="0 0 90 90"><circle cx="45" cy="45" r="43" fill="none" stroke="#ccc"/>
    <circle cx="45" cy="45" r="12" fill="none" stroke="#17a86a" stroke-width="2"/>
    <text x="45" y="50" text-anchor="middle" font-family="Open Sans,sans-serif" font-size="14" font-weight="600" fill="#17a86a">$</text></svg>
  <h3>Paid</h3><p>Payment into your bank account<br>within two days</p>
</div>

<div class="divider"></div>

<section class="get-market">
  <h2>Get Market</h2>
  <p>Pellentesque convallis molestie enim sit amet efficitur. Etiam id imperdiet lectus. Vivamus lacus justo, ultrices nec erat in, euismod iaculis mauris. Vivamus eleifend vitae nulla vel malesuada. In ac malesuada lacus, et consectetur ante. Fusce vitae lectus sit amet mi pulvinar maximus.</p>
  <span class="go-btn">Go</span>
</section>
<div class="market-mark" role="img" aria-label="Hand-drawn dark spiral target illustration"></div>

<section class="faq">
  <h2 class="section-title">FAQs</h2>
  <div class="faq-grid">
    <div class="faq-item"><h4>Aenean facilisis tincidunt lectus, dictum luctus feugiat nibh?</h4><p>Vivamus eleifend vitae nulla vel malesuada. In ac malesuada lacus, et consectetur ante.</p></div>
    <div class="faq-item"><h4>Nulla facilisi. Etiam vel massa elementum, bibendum tellus?</h4><p>Fusce vitae lectus sit amet mi pulvinar maximus. Aenean placerat, nibh vel accumsan aliquet, magna nibh accumsan nibh, ac tempus.</p></div>
    <div class="faq-item"><h4>Pellentesque convallis molestie enim sit amet efficitur?</h4><p>Vivamus eleifend vitae nulla vel malesuada. In ac malesuada lacus, et consectetur ante.</p></div>
    <div class="faq-item"><h4>Proin a dolor mauris</h4><p>Donec molestie nisi et tellus hendrerit vehicula. Nunc eu ligula sed quam pulvinar maximus in vitae eros. Proin porta fermentum ipsum, vel porttitor turpis venenatis luctus. Vivamus volutpat eu sapien quis tempus. Aenean feugiat viverra lorem ac sagittis.</p></div>
    <div class="faq-item"><h4>Mauris suscipit felis id nunc elementum varius?</h4><p>Phasellus blandit quam a ipsum gravida dapibus. Cras sed augue tortor. Suspendisse elit ligula, iaculis dignissim justo eu, vestibulum venenatis elit. Sed egestas, nisl id cursus ultricies.</p></div>
    <div class="faq-item"><h4>Donec vestibulum odio sem, ac laoreet ullamcorper?</h4><p>Vivamus eleifend vitae nulla vel malesuada. In ac malesuada lacus, et consectetur ante.</p></div>
  </div>
</section>

<section class="about">
  <h2 class="section-title">About us</h2>
  <p>Nam et tortor in ante iaculis porttitor in luctus mi. Vivamus gravida sem a pretium euismod. Nam lobortis, purus et fringilla tempus, risus eros dignissim diam, eget finibus sem risus sit amet eros. Vestibulum facilisis dolor at purus tincidunt porta. Nam fringilla nulla vel nisl condimentum, dapibus condimentum enim porta. Phasellus blandit quam a ipsum gravida dapibus. Cras sed augue tortor. Suspendisse elit ligula, iaculis dignissim justo eu, vestibulum venenatis elit.&nbsp; Sed egestas, nisl id cursus ultricies, turpis orci rhoncus odio, id tristique odio ex in lacus.</p>
</section>

<footer class="site-footer">
  <div class="footer-links"><a href="#">Home</a><span>|</span><a href="#">Quote</a><span>|</span><a href="#">Order</a><span>|</span><a href="#">Testimonials</a><span>|</span><a href="#">Contact</a><span>|</span><a href="#">Login</a></div>
  <div class="copyright">Copyright © 2015&nbsp; The Handset Bazaar.&nbsp; All rights reserved.</div>
  <div class="contact">Call : 555 204 7731&nbsp; /&nbsp; Email : info@thehandsetbazaar.com</div>
  <div class="socials">
    <span class="social"><i></i>QV</span>
    <span class="social"><i></i>Chirpel</span>
    <span class="social"><i></i>Work Nest</span>
  </div>
</footer>
</body>
</html>
```